Saltmarsh Valley Lending Flyer

I would like our main long logo with the bird and words Saltmarsh Valley Lending with pictures of what we finance along the bottom.
Car , 4x4 , boat, excavator , Cash Loans and houses
Needs to look good on leaflet and large signage.
Simple but cool looking so it stands out.

```html
<!DOCTYPE html>
<html lang="en">
<head>
<meta charset="utf-8">
<title>Saltmarsh Valley Lending Flyer</title>
<link rel="stylesheet" href="https://fonts.googleapis.com/css2?family=Cinzel:wght@400;600&display=swap">
<style>
  :root {
    --page-bg: #bdbdbd;
    --banner-bg: #231f20;
    --frame-orange: #f27a1a;
    --disc-light: #f6923f;
    --disc-dark: #ef7d1c;
    --ink-white: #ffffff;
  }
  * { margin: 0; padding: 0; box-sizing: border-box; }
  html, body {
    width: 1200px; height: 524px; overflow: hidden;
    background: var(--page-bg);
  }
  .flyer {
    position: absolute; left: 30px; top: 73px;
    width: 1140px; height: 378px;
    background: var(--banner-bg);
    font-family: "Cinzel", "Times New Roman", serif;
    color: var(--ink-white);
  }
  .flyer-frame {
    position: absolute; inset: 7px;
    border: 3px solid var(--frame-orange);
  }
  .brand-square {
    position: absolute; left: 69px; top: 50px;
    width: 71px; height: 78px;
    border: 3px solid var(--ink-white);
  }
  .brand-name {
    position: absolute; left: 180px; top: 52px;
    font-size: 40px; font-weight: 400; line-height: 37px;
    letter-spacing: 0.5px;
  }
  .service {
    position: absolute; top: 164px;
    width: 152px; height: 152px;
    margin-left: -76px;
    border-radius: 50%;
    background: var(--disc-light);
    overflow: hidden;
  }
  .service::after {
    content: ""; position: absolute;
    left: -40%; top: 58%;
    width: 180%; height: 120%;
    border-radius: 50%;
    background: var(--disc-dark);
  }
  .service-icon {
    position: absolute; left: 26px; top: 26px;
    width: 100px; height: 100px; z-index: 1;
    fill: none; stroke: var(--ink-white);
    stroke-width: 3; stroke-linecap: round; stroke-linejoin: round;
  }
  .service-label {
    position: absolute; top: 324px;
    transform: translateX(-50%);
    font-size: 26px; font-weight: 600; white-space: nowrap;
    letter-spacing: 0.5px;
  }
</style>
</head>
<body>
<main class="flyer">
  <div class="flyer-frame"></div>

  <div class="brand-square"></div>
  <h1 class="brand-name">Saltmarsh Valley<br>Lending</h1>

  <div class="service" style="left:104px">
    <svg class="service-icon" viewBox="0 0 100 100" aria-hidden="true">
      <path d="M22 48 L30 26 H70 L78 48"/>
      <path d="M30 46 L35 32 H65 L70 46 Z"/>
      <rect x="14" y="48" width="72" height="24" rx="6"/>
      <ellipse cx="27" cy="58" rx="7" ry="4"/>
      <ellipse cx="73" cy="58" rx="7" ry="4"/>
      <rect x="40" y="55" width="20" height="8" rx="2"/>
      <path d="M20 72 V82 H32 V72 M68 72 V82 H80 V72"/>
      <path d="M14 46 H8 M86 46 H92"/>
    </svg>
  </div>
  <span class="service-label" style="left:104px">Car</span>

  <div class="service" style="left:290px">
    <svg class="service-icon" viewBox="0 0 100 100" aria-hidden="true">
      <path d="M8 66 V52 L24 46 L36 28 H86 V66 H76 M58 66 H34 M16 66 H8"/>
      <path d="M40 34 H58 V46 H30 Z"/>
      <path d="M64 34 H80 V46 H64 Z"/>
      <circle cx="25" cy="68" r="9"/>
      <circle cx="67" cy="68" r="9"/>
    </svg>
  </div>
  <span class="service-label" style="left:290px">4x4</span>

  <div class="service" style="left:477px">
    <svg class="service-icon" viewBox="0 0 100 100" aria-hidden="true">
      <path d="M8 56 H92 L80 80 H22 Z"/>
      <rect x="26" y="40" width="40" height="16"/>
      <rect x="34" y="24" width="12" height="16"/>
      <path d="M34 30 H46"/>
      <circle cx="38" cy="67" r="3"/>
      <circle cx="50" cy="67" r="3"/>
      <circle cx="62" cy="67" r="3"/>
    </svg>
  </div>
  <span class="service-label" style="left:477px">Boat</span>

  <div class="service" style="left:664px">
    <svg class="service-icon" viewBox="0 0 100 100" aria-hidden="true">
      <rect x="30" y="74" width="52" height="14" rx="7"/>
      <circle cx="38" cy="81" r="2"/>
      <circle cx="56" cy="81" r="2"/>
      <circle cx="74" cy="81" r="2"/>
      <rect x="40" y="52" width="36" height="22"/>
      <rect x="48" y="36" width="22" height="16"/>
      <path d="M40 60 L22 14 L12 18 L14 58"/>
      <path d="M10 58 H20 L16 70 H8 Z"/>
      <path d="M76 70 H88 L92 80"/>
    </svg>
  </div>
  <span class="service-label" style="left:664px">Excavator</span>

  <div class="service" style="left:849px">
    <svg class="service-icon" viewBox="0 0 100 100" aria-hidden="true">
      <circle cx="52" cy="26" r="16"/>
      <path d="M52 16 V36 M57 20 C52 16 46 18 47 23 C48 27 57 25 57 30 C57 35 50 36 46 32"/>
      <rect x="6" y="58" width="12" height="26"/>
      <path d="M18 62 C30 56 42 58 52 64 H62 C66 64 66 72 60 72 H46"/>
      <path d="M18 80 H54 L90 60 C94 56 90 50 84 54 L64 66"/>
    </svg>
  </div>

  <div class="service" style="left:1035px">
    <svg class="service-icon" viewBox="0 0 100 100" aria-hidden="true">
      <path d="M20 40 L52 12 L84 40 M28 34 V58 H76 V34"/>
      <path d="M68 20 V26"/>
      <circle cx="52" cy="40" r="11"/>
      <path d="M52 33 V47 M55 36 C52 34 48 35 49 38 C50 41 56 40 55 43 C54 46 50 46 48 44"/>
      <rect x="6" y="68" width="10" height="20"/>
      <path d="M16 70 C28 64 40 66 48 72 H58 C62 72 62 78 56 78 H44"/>
      <path d="M16 86 H52 L86 68 C90 64 86 58 80 62 L62 74"/>
    </svg>
  </div>
  <span class="service-label" style="left:950px">Cash - Loans - House</span>
</main>
</body>
</html>
```